Brindle Structures Construction Company Seeking Modern Website

We are a small construction company wanting to create a web presence. We don't have much in the way of current content but will get photos as they come in. Attached is a picture of our business card.
The pages we would like on the menu are:
Home
Portfolio
Product Specs
Testimonials
Our Process
Contact
Some designs we like are:
http://www.tovenquarnsheds.example/
http://www.qzrsheds.example/
http://pannowsheds.example/
http://wistenhalls.example/
Not much requirements other than that so feel free to be creative!
Updates
Target Market(s)
Construction
Commercial and Residential Buildings
Industry/Entity Type
Construction Company
Number of Pages Required
5+ page
Look and feel

```html
<!DOCTYPE html>
<html lang="en">
<head>
<meta charset="utf-8">
<title>Brindle Structures</title>
<link href="https://fonts.googleapis.com/css2?family=Open+Sans:wght@400;600;700&display=swap" rel="stylesheet">
<style>
:root{
  --blue:#2a9fd6;
  --logo:#1d6fd1;
  --orange:#f39c12;
  --green:#2ecc71;
  --ink:#333;
  --muted:#888;
  --line:#d9d9d9;
  --grey-bg:#f2f2f2;
  --footer:#1f1f1f;
  --footer-bar:#141414;
  --white:#fff;
}
*{box-sizing:border-box;margin:0;padding:0}
html,body{width:1200px;height:4356px;overflow:hidden}
body{font-family:"Open Sans",Arial,sans-serif;color:var(--ink);background:var(--white);position:relative}
.abs{position:absolute}

/* header + hero */
.hero{top:0;left:0;width:1200px;height:512px;background:linear-gradient(135deg,#6b5a48 0%,#9c8672 35%,#5e4c3b 70%,#3b2f25 100%)}
.topbar{top:0;left:0;width:1200px;height:60px;background:rgba(0,0,0,.35)}
.logo{left:96px;top:12px;font-size:30px;font-weight:700;color:var(--logo);letter-spacing:-.5px;white-space:nowrap}
.top-links{right:40px;top:20px;display:flex;gap:22px;align-items:center;color:var(--white);font-size:15px;white-space:nowrap}
.top-links svg{display:block}
.hero-title{top:150px;left:0;width:1200px;text-align:center;color:var(--white);font-size:31px;letter-spacing:2px;line-height:44px;font-weight:400}
.hero-btns{top:252px;left:0;width:1200px;display:flex;justify-content:center;gap:14px}
.btn-ghost{border:2px solid var(--white);color:var(--white);font-size:15px;padding:6px 14px;border-radius:3px;white-space:nowrap}
.hero-dots{right:72px;top:450px;display:flex;gap:10px}
.hero-dots span{width:12px;height:12px;border-radius:50%;border:2px solid var(--white)}
.hero-dots span.on{background:var(--white)}

/* page menu bar */
.menu{top:512px;left:108px;width:984px;height:88px;display:flex;border-bottom:1px solid var(--line)}
.menu-item{flex:1;border-right:1px solid var(--line);display:flex;flex-direction:column;align-items:center;justify-content:center;gap:8px;font-size:13px;color:#555;white-space:nowrap}
.menu-item:first-child{border-left:1px solid var(--line)}
.menu-item.active{color:var(--blue)}

/* section titles */
.sec-title{left:0;width:1200px;display:flex;align-items:center;justify-content:center;gap:24px;font-size:30px;color:#444;font-weight:400;white-space:nowrap}
.sec-title::before,.sec-title::after{content:"";width:180px;height:2px;background:#bbb}

/* popular */
.pop-card{top:732px;height:316px;box-shadow:0 1px 6px rgba(0,0,0,.15);background:var(--white)}
.pop-img{width:100%;height:236px}
.price{position:absolute;right:0;top:96px;background:var(--blue);color:var(--white);font-size:14px;font-weight:600;padding:6px 10px}
.pop-card h3{font-size:17px;color:var(--blue);font-weight:400;margin:12px 16px 2px}
.pop-card p{font-size:14px;margin:0 16px}

/* services */
.services{top:1120px;left:0;width:1200px;height:440px;background:var(--grey-bg)}
.sub{left:0;width:1200px;text-align:center;font-size:15px;color:#666}
.svc{width:440px;display:flex;gap:22px}
.svc-ic{width:52px;height:52px;border-radius:50%;border:2px solid #bbb;flex:none;display:flex;align-items:center;justify-content:center}
.svc h4{font-size:15px;font-weight:600;color:#555;margin:4px 0 6px}
.svc p{font-size:13px;line-height:21px;color:#777}

/* features band */
.band{top:1560px;left:0;width:1200px;height:340px;background:linear-gradient(90deg,#4e4538 0%,#8b7d6a 40%,#b6a68e 60%,#6d5f4d 100%)}
.feat-box{top:1632px;left:788px;width:320px;height:228px;background:rgba(30,30,30,.85);color:var(--white);padding:24px 26px}
.feat-box h4{font-size:17px;font-weight:400;letter-spacing:1px;margin-bottom:12px}
.feat-box p{font-size:13px;line-height:20px;color:#ddd}
.btn-small{display:inline-block;border:1px solid var(--white);font-size:12px;padding:4px 10px;margin-top:14px}

/* app */
.phone{top:1960px;left:232px;width:220px;height:420px;border-radius:30px;background:#111}
.screen{position:absolute;left:14px;top:56px;width:192px;height:304px;background:linear-gradient(160deg,#e8e4d8,#cfd8c4 50%,#d9d2c0)}
.phone .cam{position:absolute;left:90px;top:26px;width:40px;height:6px;border-radius:3px;background:#333}
.phone .home{position:absolute;left:94px;top:374px;width:32px;height:32px;border-radius:50%;border:2px solid #333}
.app-text{top:1966px;left:612px;width:460px}
.app-text h3{font-size:18px;font-weight:700;color:#444;line-height:28px}
.app-text h3 span{color:var(--orange)}
.app-text h5{font-size:16px;font-weight:600;color:var(--orange);margin:20px 0 8px}
.app-text p{font-size:13px;line-height:20px;color:#777}
.btn-outline{display:inline-block;border:2px solid var(--blue);color:var(--blue);font-size:14px;padding:5px 14px;margin-top:22px}

/* portfolio gallery */
.gallery{top:2460px;left:0;width:1200px;height:500px;background:var(--grey-bg)}
.g-card{top:2592px;height:348px;width:228px;background:var(--white);box-shadow:0 1px 5px rgba(0,0,0,.12)}
.g-img{height:168px}
.g-body{padding:12px 14px;position:relative}
.g-body .star{position:absolute;left:14px;top:14px}
.g-body h4{margin-left:54px;font-size:15px;font-weight:600}
.g-body .rev{margin-left:54px;font-size:12px;color:var(--muted)}
.g-body .spec{font-size:13px;margin-top:16px;color:#555}
.g-body .amt{font-size:13px;margin-top:6px;color:#555}
.btn-tiny{display:inline-block;border:1px solid var(--blue);color:var(--blue);font-size:12px;padding:2px 8px;margin-top:10px}

/* testimonials */
.quote{width:400px}
.quote p{font-size:13px;line-height:20px;color:#666;padding-bottom:14px;border-bottom:2px solid #bbb}
.person{display:flex;align-items:center;gap:14px;white-space:nowrap}
.avatar{width:52px;height:52px;border-radius:50%;background:linear-gradient(135deg,#d9b8a0,#8a6a58)}
.person b{display:block;font-size:15px;color:var(--blue);font-weight:600}
.person small{font-size:12px;color:var(--muted)}

/* partners */
.partners{top:3600px;left:0;width:1200px;height:340px;border-top:1px solid #e6e6e6}
.badge{width:104px;height:40px;border-radius:6px;background:#d6d6d6}

/* footer */
.footer{top:3940px;left:0;width:1200px;height:352px;background:var(--footer)}
.f-col{top:3980px;color:#bbb;width:230px}
.f-col h4{color:var(--white);font-size:20px;font-weight:400;margin-bottom:16px;white-space:nowrap}
.f-col li{list-style:none;font-size:13px;line-height:26px;white-space:nowrap}
.socials{top:4212px;left:850px;display:flex;gap:14px}
.socials span{width:18px;height:18px;border-radius:50%;background:#aaa}
.f-bar{top:4292px;left:0;width:1200px;height:64px;background:var(--footer-bar);color:#999;font-size:13px;display:flex;align-items:center;justify-content:flex-end;padding-right:130px}
</style>
</head>
<body>

<!-- hero -->
<div class="abs hero" role="img" aria-label="Photo of a finished interior with warm wooden walls"></div>
<div class="abs topbar"></div>
<div class="abs logo">Brindle Structures</div>
<div class="abs top-links">
  <span style="display:flex;gap:6px;align-items:center"><svg width="14" height="14" viewBox="0 0 24 24"><path d="M6 2l4 4-2 3c1 3 4 6 7 7l3-2 4 4-3 4C10 22 2 14 2 5z" fill="#fff"/></svg>01-555-010-200</span>
  <span style="display:flex;gap:6px;align-items:center"><svg width="14" height="14" viewBox="0 0 24 24"><circle cx="12" cy="8" r="5" fill="#fff"/><path d="M3 22c0-6 18-6 18 0z" fill="#fff"/></svg>Login</span>
  <svg width="18" height="18" viewBox="0 0 24 24"><circle cx="10" cy="10" r="7" stroke="#fff" stroke-width="3" fill="none"/><path d="M15 15l7 7" stroke="#fff" stroke-width="3"/></svg>
  <svg width="20" height="18" viewBox="0 0 24 20"><path d="M2 3h20M2 10h20M2 17h20" stroke="#fff" stroke-width="3"/></svg>
</div>
<h1 class="abs hero-title">LOREM IPSUM IS NOT SIMPLY RANDOM TEXT. IT<br>HAS ROOTS IN A PIECE OF CLASSICAL</h1>
<div class="abs hero-btns"><span class="btn-ghost">View Portfolio</span><span class="btn-ghost">Get a Free Quote</span></div>
<div class="abs hero-dots"><span class="on"></span><span></span><span></span></div>

<!-- page menu -->
<nav class="abs menu">
  <div class="menu-item active"><svg width="30" height="26" viewBox="0 0 30 26"><path d="M3 13L15 3l12 10M7 11v13h16V11" stroke="currentColor" stroke-width="2" fill="none"/></svg>Home</div>
  <div class="menu-item"><svg width="30" height="26" viewBox="0 0 30 26"><rect x="4" y="3" width="9" height="9" stroke="#888" stroke-width="2" fill="none"/><rect x="17" y="3" width="9" height="9" stroke="#888" stroke-width="2" fill="none"/><rect x="4" y="15" width="9" height="9" stroke="#888" stroke-width="2" fill="none"/><rect x="17" y="15" width="9" height="9" stroke="#888" stroke-width="2" fill="none"/></svg>Portfolio</div>
  <div class="menu-item"><svg width="30" height="26" viewBox="0 0 30 26"><path d="M7 2h11l5 5v17H7z" stroke="#888" stroke-width="2" fill="none"/><path d="M10 12h10M10 16h10M10 20h6" stroke="#888" stroke-width="2"/></svg>Product Specs</div>
  <div class="menu-item"><svg width="30" height="26" viewBox="0 0 30 26"><path d="M3 4h24v14H12l-6 5v-5H3z" stroke="#888" stroke-width="2" fill="none"/></svg>Testimonials</div>
  <div class="menu-item"><svg width="30" height="26" viewBox="0 0 30 26"><circle cx="15" cy="13" r="4" stroke="#888" stroke-width="2" fill="none"/><path d="M15 2v5M15 19v5M4 13h5M21 13h5M7 5l3 3M20 18l3 3M7 21l3-3M20 8l3-3" stroke="#888" stroke-width="2"/></svg>Our Process</div>
  <div class="menu-item"><svg width="30" height="26" viewBox="0 0 30 26"><rect x="3" y="5" width="24" height="16" rx="1" stroke="#888" stroke-width="2" fill="none"/><path d="M3 6l12 9 12-9" stroke="#888" stroke-width="2" fill="none"/></svg>Contact</div>
</nav>

<!-- most popular -->
<h2 class="abs sec-title" style="top:618px">Most Popular</h2>
<article class="abs pop-card" style="left:108px;width:292px">
  <div class="pop-img" role="img" aria-label="Photo of a completed house with a gabled roof" style="background:linear-gradient(180deg,#b9d0e6 0%,#d8dde0 45%,#9a8f82 70%,#6f8a52 100%)"></div>
  <span class="price">45,000$</span>
  <h3>Contrary to popular</h3><p>Lorem ipsum</p>
</article>
<article class="abs pop-card" style="left:452px;width:296px">
  <div class="pop-img" role="img" aria-label="Photo of a large white residential building with lawn" style="background:linear-gradient(180deg,#6ea3d8 0%,#b7cde0 40%,#e4e2dc 60%,#5f8a3a 100%)"></div>
  <span class="price">45,000$</span>
  <h3>Contrary to popular</h3><p>Lorem ipsum</p>
</article>
<article class="abs pop-card" style="left:784px;width:308px">
  <div class="pop-img" role="img" aria-label="Photo of an open finished interior" style="background:linear-gradient(160deg,#5b4636 0%,#8a6f58 45%,#c8b49a 75%,#3c2e24 100%)"></div>
  <span class="price">45,000$</span>
  <h3>Contrary to popular</h3><p>Lorem ipsum</p>
</article>

<!-- services -->
<section class="abs services"></section>
<h2 class="abs sec-title" style="top:1160px">Services</h2>
<p class="abs sub" style="top:1216px">Lorem Ipsum is simply dummy text of the printing and typesetting industry.</p>
<div class="abs svc" style="left:120px;top:1284px"><div class="svc-ic"><svg width="20" height="20" viewBox="0 0 24 24"><circle cx="12" cy="8" r="5" fill="#999"/><path d="M3 22c0-7 18-7 18 0z" fill="#999"/></svg></div><div><h4>UT WISI ENIM AD</h4><p>Contrary to popular belief, Lorem Ipsum is not simply<br>random text. It has roots in a piece of<br>classical Latin literature from many years ago.</p></div></div>
<div class="abs svc" style="left:640px;top:1284px"><div class="svc-ic"><svg width="20" height="20" viewBox="0 0 24 24"><path d="M4 20C4 10 10 4 20 4c0 10-6 16-16 16zM4 20L14 10" stroke="#999" stroke-width="2" fill="none"/></svg></div><div><h4>UT WISI ENIM AD</h4><p>Contrary to popular belief, Lorem Ipsum is not simply<br>random text. It has roots in a piece of<br>classical Latin literature from many years ago.</p></div></div>
<div class="abs svc" style="left:120px;top:1392px"><div class="svc-ic"><svg width="22" height="22" viewBox="0 0 24 24"><circle cx="12" cy="12" r="4" stroke="#999" stroke-width="2" fill="none"/><path d="M12 2v4M12 18v4M2 12h4M18 12h4M5 5l3 3M16 16l3 3M5 19l3-3M16 8l3-3" stroke="#999" stroke-width="2"/></svg></div><div><h4>UT WISI ENIM AD</h4><p>Contrary to popular belief, Lorem Ipsum is not simply<br>random text. It has roots in a piece of<br>classical Latin literature from many years ago.</p></div></div>
<div class="abs svc" style="left:640px;top:1392px"><div class="svc-ic"><svg width="20" height="22" viewBox="0 0 20 24"><path d="M3 2h9l5 5v15H3z" stroke="#999" stroke-width="2" fill="none"/><path d="M6 12h8M6 16h8" stroke="#999" stroke-width="2"/></svg></div><div><h4>UT WISI ENIM AD</h4><p>Contrary to popular belief, Lorem Ipsum is not simply<br>random text. It has roots in a piece of<br>classical Latin literature from many years ago.</p></div></div>

<!-- features band -->
<div class="abs band" role="img" aria-label="Photo of a furnished room inside a finished building"></div>
<div class="abs feat-box">
  <h4>THE BEST FEATURES</h4>
  <p>Contrary to popular belief, Lorem Ipsum is not simply random text. It has roots in a piece of classical Latin literature from 45 BC, making it over 2000 years old.</p>
  <span class="btn-small">Read More</span>
</div>

<!-- app -->
<div class="abs phone"><span class="cam"></span><div class="screen" role="img" aria-label="Map view of the project tracking app on a phone screen"></div><span class="home"></span></div>
<div class="abs app-text">
  <h3>FOLLOW YOUR BUILD EVERYWHERE BY<br><span>BRINDLE TRACKER MOBILE APP</span></h3>
  <h5>Custom Location Tracker</h5>
  <p>There are many variations of passages of Lorem<br>Ipsum available, but the majority.</p>
  <h5>Map Search</h5>
  <p>There are many variations of passages of Lorem<br>Ipsum available, but the majority.</p>
  <h5>Quick Details</h5>
  <p>There are many variations of passages of Lorem<br>Ipsum available, but the majority.</p>
  <span class="btn-outline">Download the App</span>
</div>

<!-- project gallery -->
<section class="abs gallery"></section>
<h2 class="abs sec-title" style="top:2512px">Project Gallery</h2>
<article class="abs g-card" style="left:108px"><div class="g-img" role="img" aria-label="Photo of a completed commercial tower against blue sky" style="background:linear-gradient(180deg,#4d8fd0,#a9c7e4 50%,#a0523b)"></div><div class="g-body"><svg class="star" width="34" height="34" viewBox="0 0 24 24"><path d="M12 2l3 7 7 .6-5.4 4.7 1.7 7.2L12 17.8 5.7 21.5l1.7-7.2L2 9.6 9 9z" fill="var(--green)"/></svg><h4>Venice</h4><div class="rev">No Reviews</div><div class="spec">2, 3, 4 Bay Buildings</div><div class="amt">$50,000</div><span class="btn-tiny">See Details</span></div></article>
<article class="abs g-card" style="left:360px"><div class="g-img" role="img" aria-label="Photo of a colourful building facade" style="background:linear-gradient(135deg,#7bb33d,#d8d040 50%,#3a7fc0)"></div><div class="g-body"><svg class="star" width="34" height="34" viewBox="0 0 24 24"><path d="M12 2l3 7 7 .6-5.4 4.7 1.7 7.2L12 17.8 5.7 21.5l1.7-7.2L2 9.6 9 9z" fill="var(--green)"/></svg><h4>Venice</h4><div class="rev">No Reviews</div><div class="spec">2, 3, 4 Bay Buildings</div><div class="amt">$50,000</div><span class="btn-tiny">See Details</span></div></article>
<article class="abs g-card" style="left:612px"><div class="g-img" role="img" aria-label="Photo of a finished building lit at sunset" style="background:linear-gradient(180deg,#e0a030,#c96a20 50%,#3d2a1e)"></div><div class="g-body"><svg class="star" width="34" height="34" viewBox="0 0 24 24"><path d="M12 2l3 7 7 .6-5.4 4.7 1.7 7.2L12 17.8 5.7 21.5l1.7-7.2L2 9.6 9 9z" fill="var(--green)"/></svg><h4>Venice</h4><div class="rev">No Reviews</div><div class="spec">2, 3, 4 Bay Buildings</div><div class="amt">$50,000</div><span class="btn-tiny">See Details</span></div></article>
<article class="abs g-card" style="left:864px"><div class="g-img" role="img" aria-label="Photo of a glass office building" style="background:linear-gradient(180deg,#dfe8ef,#8fb1cc 60%,#5a7b96)"></div><div class="g-body"><svg class="star" width="34" height="34" viewBox="0 0 24 24"><path d="M12 2l3 7 7 .6-5.4 4.7 1.7 7.2L12 17.8 5.7 21.5l1.7-7.2L2 9.6 9 9z" fill="var(--green)"/></svg><h4>Venice</h4><div class="rev">No Reviews</div><div class="spec">2, 3, 4 Bay Buildings</div><div class="amt">$50,000</div><span class="btn-tiny">See Details</span></div></article>

<!-- testimonials -->
<h2 class="abs sec-title" style="top:3072px">Testimonials</h2>
<div class="abs quote" style="left:100px;top:3172px"><p>Duis aute irure dolor in reprehenderit in voluptate velit esse cillum dolore eu fugiat nulla pariatur.</p></div>
<div class="abs person" style="left:310px;top:3290px"><div class="avatar" role="img" aria-label="Client portrait"></div><div><b>Rowan T. Calder</b><small>Ut enim ad minim</small></div></div>
<div class="abs quote" style="left:620px;top:3252px"><p>Duis aute irure dolor in reprehenderit in voluptate velit esse cillum dolore eu fugiat nulla pariatur.</p></div>
<div class="abs person" style="left:880px;top:3366px"><div class="avatar" role="img" aria-label="Client portrait"></div><div><b>Nora L. Fenwick</b><small>Ut enim ad minim</small></div></div>
<div class="abs quote" style="left:100px;top:3380px"><p>Duis aute irure dolor in reprehenderit in voluptate velit esse cillum dolore eu fugiat nulla pariatur.</p></div>
<div class="abs person" style="left:330px;top:3490px"><div class="avatar" role="img" aria-label="Client portrait"></div><div><b>Ada K. Pellow</b><small>Ut enim ad minim</small></div></div>

<!-- partners -->
<section class="abs partners"></section>
<h2 class="abs sec-title" style="top:3672px">Our Partners</h2>
<div class="abs" style="top:3756px;left:220px;width:760px;display:flex;justify-content:space-between"><span class="badge"></span><span class="badge"></span><span class="badge"></span><span class="badge"></span><span class="badge"></span></div>
<div class="abs" style="top:3826px;left:220px;width:760px;display:flex;justify-content:space-between"><span class="badge"></span><span class="badge"></span><span class="badge"></span><span class="badge"></span><span class="badge"></span></div>

<!-- footer -->
<footer class="abs footer"></footer>
<div class="abs f-col" style="left:108px"><h4>Our Company</h4><ul><li>Home</li><li>Portfolio</li><li>Product Specs</li><li>Testimonials</li><li>Our Process</li><li>Contact</li></ul></div>
<div class="abs f-col" style="left:358px"><h4>Work With Us</h4><ul><li>Subcontractors</li><li>Suppliers</li><li>Careers</li><li>Site Safety</li><li>Terms &amp; Conditions</li><li>Privacy Policy</li></ul></div>
<div class="abs f-col" style="left:608px"><h4>Customer Support</h4><ul><li>Mon-Fri, 8AM-5PM</li><li>Call: 01-555-010-200</li><li>Request a Quote</li><li>Frequently Asked Questions</li><li>Give Us Feedback</li><li>Warranty Claims</li></ul></div>
<div class="abs f-col" style="left:858px"><h4>Building Services</h4><ul><li>Residential Buildings</li><li>Commercial Buildings</li><li>Pole Barns</li><li>Garages &amp; Shops</li><li>Renovations</li></ul></div>
<div class="abs socials"><span></span><span></span><span></span><span></span><span></span></div>
<div class="abs f-bar">© 2015 Brindle Structures. All Rights Reserved</div>

</body>
</html>
```